Survey App for phone users trying a new phone with Dual connectivity

Survey App Brief<br/>Design For an Android Survey App for users' feedback on Call, SMS, Data and Streaming Experience on their Mobile phones.<br/><br/>Purpose of the App<br/>To ensure that the user's experience is not impacted by the network switching between two network on the special mobile phones they newly started using.<br/><br/>App Requirements:<br/>First screen: The registration screen, where the user needs to enter the following:<br/>Name: text box<br/>Phone Number: text box<br/>Group Number : <br/><br/>An information text:<br/>By Registering I agree to participate in the Survey.<br/><br/>Register: Button<br/><br/>Start Screen - Survey screens (next time user open the App this will be the first screen):<br/>We need feedback for 4 indicators:<br/>Call Experience<br/>SMS Experience<br/>Data Experience<br/>Streaming Experience<br/><br/>Each Experience can be in the form of a questionnaire or Satisfied/ Somewhat Satisfied / Extremely Satisfied form with radio buttons or on a scale of 1 to 5. We need to ensure that the format used is very professional.<br/><br/>An optional text box for the user to enter the comment in a free format.<br/><br/>This can be done in 4 different screens or in one single screen if it does not give a clumsy look.<br/><br/>A Send button at the end to submit the Survey.<br/><br/>We need a burger menu at the top left corner of this screen, which when expanded will provide 5 options:<br/>Edit User Profile<br/>Survey interval Timer<br/>FAQ<br/>Exit<br/>About<br/><br/><br/>Please ensure that the app is simple, friendly, lively and professional at the same time so that it ignites an interest in the user to use the app.<br/>Use Logo as appropriate.
Telecommunications
Colors
Designer to choose colors to be used in the design.

```html
<!DOCTYPE html>
<html lang="en">
<head>
<meta charset="utf-8">
<title>Meridian Signal – Survey App Screens</title>
<link href="https://fonts.googleapis.com/css2?family=Poppins:wght@400;500;600;700&display=swap" rel="stylesheet">
<style>
:root{
  --page:#f5f6fa;
  --deco:#eceff7;
  --screen:#ffffff;
  --ink:#2b3656;
  --muted:#8a93aa;
  --field:#eef1f7;
  --primary:#3aa8e4;
  --primary-deep:#1f86d6;
  --primary-light:#55c6f0;
  --track:#e3e8f1;
  --highlight:#edf5fd;
}
*{box-sizing:border-box;margin:0;padding:0}
html,body{width:1200px;height:3196px;overflow:hidden}
body{background:var(--page);font-family:"Poppins",sans-serif;color:var(--ink);position:relative}
.deco{position:absolute;border-radius:50%;background:var(--deco)}
.deco-right{width:1300px;height:1300px;left:560px;top:380px}
.deco-left{width:1100px;height:1100px;left:-560px;top:2240px}
.deco-top{width:700px;height:700px;left:820px;top:-420px;background:#f0f2f9}

.page-brand{position:absolute;left:96px;top:44px}
.brand{display:flex;align-items:center;gap:8px}
.brand-dot{width:26px;height:26px;border-radius:50%;background:var(--primary);flex:none}
.brand-name{font-size:10px;font-weight:600;line-height:1.15;letter-spacing:.06em;text-transform:uppercase;color:var(--primary)}

.screen{position:absolute;background:var(--screen);overflow:hidden;box-shadow:0 10px 40px rgba(40,60,120,.08)}
.mini{border-radius:30px;top:160px;width:260px;height:540px}
.mini .inner{transform-origin:0 0;position:absolute;left:0;top:0}
.status{position:absolute;left:0;right:0;top:0;height:40px;display:flex;justify-content:space-between;align-items:center;padding:0 22px;font-size:14px;font-weight:600;color:#111}
.status svg{display:block}

/* registration */
.reg{width:400px;height:900px;position:relative;background:var(--screen)}
.reg .brand{position:absolute;left:24px;top:64px}
.reg h1{position:absolute;left:24px;top:176px;font-size:26px;font-weight:700;color:var(--ink)}
.fields{position:absolute;left:24px;top:248px;width:300px;display:flex;flex-direction:column;gap:20px}
.field{height:42px;border-radius:10px;background:var(--field);display:flex;align-items:center;gap:14px;padding:0 14px;font-size:13px;color:#a3abc0}
.field svg{flex:none}
.agree{position:absolute;left:60px;right:60px;top:676px;text-align:center;font-size:11px;line-height:1.5;color:var(--muted)}
.btn{display:flex;align-items:center;justify-content:center;height:46px;border-radius:23px;background:var(--primary);color:#fff;font-size:12px;font-weight:600;letter-spacing:.06em;text-transform:uppercase}
.reg .btn{position:absolute;left:24px;right:24px;top:744px}
.home-bar{position:absolute;left:50%;bottom:14px;width:134px;height:5px;margin-left:-67px;border-radius:3px;background:#111}

/* survey */
.survey{width:408px;height:1232px;position:relative;background:var(--screen)}
.burger{position:absolute;left:24px;top:58px;width:22px;display:flex;flex-direction:column;gap:5px}
.burger i{display:block;height:2px;border-radius:1px;background:var(--ink)}
.survey .brand{position:absolute;left:50%;top:52px;transform:translateX(-50%)}
.survey .intro{position:absolute;left:0;right:0;top:98px;text-align:center;font-size:12px;color:var(--ink)}
.cards{position:absolute;left:16px;right:16px;top:148px;display:flex;flex-direction:column;gap:34px}
.card{border-radius:12px;background:#fff;box-shadow:0 4px 18px rgba(40,60,120,.09);padding:18px 16px 20px}
.card h2{font-size:14px;font-weight:600;color:var(--ink)}
.slider{position:relative;height:8px;margin:22px 4px 0;border-radius:4px;background:var(--track)}
.slider .fill{position:absolute;left:0;top:0;bottom:0;border-radius:4px;background:linear-gradient(90deg,var(--primary-deep),var(--primary-light))}
.slider .knob{position:absolute;top:50%;width:18px;height:18px;margin:-9px 0 0 -9px;border-radius:50%;background:var(--primary-deep);box-shadow:0 2px 6px rgba(31,134,214,.4)}
.scale{display:flex;justify-content:space-between;margin-top:16px;font-size:10px;color:var(--ink)}
.note{margin-top:18px;width:86%;height:36px;border-radius:18px;background:var(--field);display:flex;align-items:center;padding:0 16px;font-size:10px;color:#a3abc0}
.survey .btn{position:absolute;left:16px;right:16px;top:1128px}

/* menu */
.menu{width:400px;height:1008px;position:relative;background:var(--screen)}
.menu .peek{position:absolute;left:328px;top:0}
.drawer{position:absolute;left:0;top:0;bottom:0;width:328px;background:#fff;box-shadow:6px 0 24px rgba(40,60,120,.12);z-index:2}
.drawer .brand{position:absolute;left:50%;top:52px;transform:translateX(-50%)}
.nav{position:absolute;left:0;right:0;top:134px;list-style:none}
.nav li{display:flex;align-items:center;gap:18px;height:58px;padding:0 24px;font-size:13px;color:var(--ink)}
.nav li.active{background:var(--highlight);color:var(--primary-deep);margin-right:12px;border-radius:0 10px 10px 0}
.nav svg{flex:none}
</style>
</head>
<body>
<div class="deco deco-top"></div>
<div class="deco deco-right"></div>
<div class="deco deco-left"></div>

<div class="page-brand brand"><span class="brand-dot"></span><span class="brand-name">Meridian<br>Signal</span></div>

<!-- ===== Mini: registration ===== -->
<div class="screen mini" style="left:120px">
 <div class="inner" style="transform:scale(.65)">
  <div class="reg">
   <div class="status"><span>9:41</span><svg width="66" height="12" viewBox="0 0 66 12"><rect x="0" y="8" width="3" height="4" rx="1" fill="#111"/><rect x="5" y="6" width="3" height="6" rx="1" fill="#111"/><rect x="10" y="3" width="3" height="9" rx="1" fill="#111"/><rect x="15" y="0" width="3" height="12" rx="1" fill="#111"/><path d="M24 4a9 9 0 0 1 12 0M26.5 6.8a5 5 0 0 1 7 0" stroke="#111" stroke-width="1.6" fill="none"/><circle cx="30" cy="10" r="1.4" fill="#111"/><rect x="41" y="1" width="22" height="10" rx="2.5" stroke="#111" fill="none"/><rect x="43" y="3" width="18" height="6" rx="1" fill="#111"/><rect x="64" y="4" width="1.5" height="4" fill="#111"/></svg></div>
   <div class="brand"><span class="brand-dot"></span><span class="brand-name">Meridian<br>Signal</span></div>
   <h1>Registration.</h1>
   <div class="fields">
    <div class="field"><svg width="16" height="16" viewBox="0 0 16 16" fill="none" stroke="#8fa0c4" stroke-width="1.4"><circle cx="8" cy="5" r="3"/><path d="M2 15c0-3.3 2.7-5 6-5s6 1.7 6 5"/></svg>Name</div>
    <div class="field"><svg width="16" height="16" viewBox="0 0 16 16" fill="none" stroke="#8fa0c4" stroke-width="1.4"><path d="M3 1.5h3l1.5 3.5-2 1.3a9 9 0 0 0 4.2 4.2l1.3-2 3.5 1.5v3c0 .8-.7 1.5-1.5 1.5A12.5 12.5 0 0 1 1.5 3c0-.8.7-1.5 1.5-1.5z"/></svg>Phone Number</div>
    <div class="field"><svg width="18" height="16" viewBox="0 0 18 16" fill="none" stroke="#8fa0c4" stroke-width="1.4"><circle cx="9" cy="5" r="2.6"/><circle cx="3.5" cy="6" r="1.8"/><circle cx="14.5" cy="6" r="1.8"/><path d="M4.5 14c0-2.6 2-4 4.5-4s4.5 1.4 4.5 4M1 13c0-1.6 1-2.6 2.5-2.6M17 13c0-1.6-1-2.6-2.5-2.6"/></svg>Group Number</div>
   </div>
   <p class="agree">By Registering I agree to participate in the Survey</p>
   <div class="btn">Register</div>
  </div>
 </div>
 <div class="home-bar" style="width:90px;margin-left:-45px;height:4px;bottom:8px"></div>
</div>

<!-- ===== Mini: survey ===== -->
<div class="screen mini" style="left:452px">
 <div class="inner" style="transform:scale(.637)">
  <div class="survey">
   <div class="status"><span>9:41</span><svg width="66" height="12" viewBox="0 0 66 12"><rect x="0" y="8" width="3" height="4" rx="1" fill="#111"/><rect x="5" y="6" width="3" height="6" rx="1" fill="#111"/><rect x="10" y="3" width="3" height="9" rx="1" fill="#111"/><rect x="15" y="0" width="3" height="12" rx="1" fill="#111"/><path d="M24 4a9 9 0 0 1 12 0M26.5 6.8a5 5 0 0 1 7 0" stroke="#111" stroke-width="1.6" fill="none"/><circle cx="30" cy="10" r="1.4" fill="#111"/><rect x="41" y="1" width="22" height="10" rx="2.5" stroke="#111" fill="none"/><rect x="43" y="3" width="18" height="6" rx="1" fill="#111"/><rect x="64" y="4" width="1.5" height="4" fill="#111"/></svg></div>
   <div class="burger"><i></i><i></i><i></i></div>
   <div class="brand"><span class="brand-dot"></span><span class="brand-name">Meridian<br>Signal</span></div>
   <p class="intro">We need feedback for survey</p>
   <div class="cards">
    <section class="card"><h2>Call Experience</h2><div class="slider"><span class="fill" style="width:75%"></span><span class="knob" style="left:75%"></span></div><div class="scale"><span>Poor</span><span>Not Well</span><span>Neutral</span><span>Satisfied</span><span>Great</span></div><div class="note">Enter for feedback</div></section>
    <section class="card"><h2>SMS Experience</h2><div class="slider"><span class="fill" style="width:50%"></span><span class="knob" style="left:50%"></span></div><div class="scale"><span>Poor</span><span>Not Well</span><span>Neutral</span><span>Satisfied</span><span>Great</span></div><div class="note">Enter for feedback</div></section>
    <section class="card"><h2>Data Experience</h2><div class="slider"><span class="fill" style="width:75%"></span><span class="knob" style="left:75%"></span></div><div class="scale"><span>Poor</span><span>Not Well</span><span>Neutral</span><span>Satisfied</span><span>Great</span></div><div class="note">Enter for feedback</div></section>
   </div>
  </div>
 </div>
 <div class="home-bar" style="width:90px;margin-left:-45px;height:4px;bottom:8px"></div>
</div>

<!-- ===== Mini: menu ===== -->
<div class="screen mini" style="left:812px">
 <div class="inner" style="transform:scale(.65)">
  <div class="menu" style="height:830px">
   <div class="drawer">
    <div class="status"><span>9:41</span></div>
    <div class="brand"><span class="brand-dot"></span><span class="brand-name">Meridian<br>Signal</span></div>
    <ul class="nav">
     <li><svg width="16" height="16" viewBox="0 0 16 16" fill="none" stroke="#5a6788" stroke-width="1.4"><rect x="1" y="1" width="5.5" height="5.5" rx="1"/><rect x="9.5" y="1" width="5.5" height="5.5" rx="1"/><rect x="1" y="9.5" width="5.5" height="5.5" rx="1"/><rect x="9.5" y="9.5" width="5.5" height="5.5" rx="1"/></svg>Dashboard</li>
     <li><svg width="16" height="16" viewBox="0 0 16 16" fill="none" stroke="#5a6788" stroke-width="1.4"><path d="M2 14l1-4 8-8 3 3-8 8z"/></svg>Edit Profiles</li>
     <li class="active"><svg width="16" height="16" viewBox="0 0 16 16" fill="none" stroke="#1f86d6" stroke-width="1.4"><circle cx="8" cy="8" r="6.5"/><path d="M8 4v4l3 2"/></svg>Survey Interval Timer</li>
     <li><svg width="16" height="16" viewBox="0 0 16 16" fill="none" stroke="#5a6788" stroke-width="1.4"><circle cx="12" cy="3.5" r="2"/><circle cx="4" cy="8" r="2"/><circle cx="12" cy="12.5" r="2"/><path d="M5.8 7l4.4-2.5M5.8 9l4.4 2.5"/></svg>Share this App</li>
     <li><svg width="16" height="16" viewBox="0 0 16 16" fill="none" stroke="#5a6788" stroke-width="1.4"><path d="M3 1.5h3l1.5 3.5-2 1.3a9 9 0 0 0 4.2 4.2l1.3-2 3.5 1.5v3c0 .8-.7 1.5-1.5 1.5A12.5 12.5 0 0 1 1.5 3c0-.8.7-1.5 1.5-1.5z"/></svg>Contact Us</li>
     <li><svg width="16" height="16" viewBox="0 0 16 16" fill="none" stroke="#5a6788" stroke-width="1.4"><circle cx="8" cy="8" r="6.5"/><path d="M6 6a2 2 0 1 1 2.8 1.8c-.5.3-.8.7-.8 1.3M8 11.5v.5"/></svg>Help</li>
     <li><svg width="16" height="16" viewBox="0 0 16 16" fill="none" stroke="#5a6788" stroke-width="1.4"><path d="M6 2H2v12h4M10 4.5L13.5 8 10 11.5M13.5 8H5.5"/></svg>Exit</li>
    </ul>
   </div>
   <div class="peek">
    <div class="survey" style="height:830px">
     <div class="burger"><i></i><i></i><i></i></div>
     <div class="cards">
      <section class="card"><h2>Call Experience</h2><div class="slider"><span class="fill" style="width:75%"></span><span class="knob" style="left:75%"></span></div><div class="scale"><span>Poor</span><span>Not Well</span><span>Neutral</span><span>Satisfied</span><span>Great</span></div><div class="note">Enter for feedback</div></section>
      <section class="card"><h2>SMS Experience</h2><div class="slider"><span class="fill" style="width:50%"></span><span class="knob" style="left:50%"></span></div><div class="scale"><span>Poor</span><span>Not Well</span><span>Neutral</span><span>Satisfied</span><span>Great</span></div><div class="note">Enter for feedback</div></section>
      <section class="card"><h2>Data Experience</h2><div class="slider"><span class="fill" style="width:75%"></span><span class="knob" style="left:75%"></span></div><div class="scale"><span>Poor</span><span>Not Well</span><span>Neutral</span><span>Satisfied</span><span>Great</span></div><div class="note">Enter for feedback</div></section>
     </div>
    </div>
   </div>
  </div>
 </div>
 <div class="home-bar" style="width:90px;margin-left:-45px;height:4px;bottom:8px"></div>
</div>

<!-- ===== Large: registration ===== -->
<div class="screen" style="left:120px;top:960px;width:400px;height:900px">
 <div class="reg">
  <div class="status"><span>9:41</span><svg width="66" height="12" viewBox="0 0 66 12"><rect x="0" y="8" width="3" height="4" rx="1" fill="#111"/><rect x="5" y="6" width="3" height="6" rx="1" fill="#111"/><rect x="10" y="3" width="3" height="9" rx="1" fill="#111"/><rect x="15" y="0" width="3" height="12" rx="1" fill="#111"/><path d="M24 4a9 9 0 0 1 12 0M26.5 6.8a5 5 0 0 1 7 0" stroke="#111" stroke-width="1.6" fill="none"/><circle cx="30" cy="10" r="1.4" fill="#111"/><rect x="41" y="1" width="22" height="10" rx="2.5" stroke="#111" fill="none"/><rect x="43" y="3" width="18" height="6" rx="1" fill="#111"/><rect x="64" y="4" width="1.5" height="4" fill="#111"/></svg></div>
  <div class="brand"><span class="brand-dot"></span><span class="brand-name">Meridian<br>Signal</span></div>
  <h1>Registration.</h1>
  <div class="fields">
   <div class="field"><svg width="16" height="16" viewBox="0 0 16 16" fill="none" stroke="#8fa0c4" stroke-width="1.4"><circle cx="8" cy="5" r="3"/><path d="M2 15c0-3.3 2.7-5 6-5s6 1.7 6 5"/></svg>Name</div>
   <div class="field"><svg width="16" height="16" viewBox="0 0 16 16" fill="none" stroke="#8fa0c4" stroke-width="1.4"><path d="M3 1.5h3l1.5 3.5-2 1.3a9 9 0 0 0 4.2 4.2l1.3-2 3.5 1.5v3c0 .8-.7 1.5-1.5 1.5A12.5 12.5 0 0 1 1.5 3c0-.8.7-1.5 1.5-1.5z"/></svg>Phone Number</div>
   <div class="field"><svg width="18" height="16" viewBox="0 0 18 16" fill="none" stroke="#8fa0c4" stroke-width="1.4"><circle cx="9" cy="5" r="2.6"/><circle cx="3.5" cy="6" r="1.8"/><circle cx="14.5" cy="6" r="1.8"/><path d="M4.5 14c0-2.6 2-4 4.5-4s4.5 1.4 4.5 4M1 13c0-1.6 1-2.6 2.5-2.6M17 13c0-1.6-1-2.6-2.5-2.6"/></svg>Group Number</div>
  </div>
  <p class="agree">By Registering I agree to participate in the Survey</p>
  <div class="btn">Register</div>
  <div class="home-bar"></div>
 </div>
</div>

<!-- ===== Large: survey ===== -->
<div class="screen" style="left:672px;top:960px;width:408px;height:1232px">
 <div class="survey">
  <div class="status"><span>9:41</span><svg width="66" height="12" viewBox="0 0 66 12"><rect x="0" y="8" width="3" height="4" rx="1" fill="#111"/><rect x="5" y="6" width="3" height="6" rx="1" fill="#111"/><rect x="10" y="3" width="3" height="9" rx="1" fill="#111"/><rect x="15" y="0" width="3" height="12" rx="1" fill="#111"/><path d="M24 4a9 9 0 0 1 12 0M26.5 6.8a5 5 0 0 1 7 0" stroke="#111" stroke-width="1.6" fill="none"/><circle cx="30" cy="10" r="1.4" fill="#111"/><rect x="41" y="1" width="22" height="10" rx="2.5" stroke="#111" fill="none"/><rect x="43" y="3" width="18" height="6" rx="1" fill="#111"/><rect x="64" y="4" width="1.5" height="4" fill="#111"/></svg></div>
  <div class="burger"><i></i><i></i><i></i></div>
  <div class="brand"><span class="brand-dot"></span><span class="brand-name">Meridian<br>Signal</span></div>
  <p class="intro">We need feedback for survey</p>
  <div class="cards">
   <section class="card"><h2>Call Experience</h2><div class="slider"><span class="fill" style="width:75%"></span><span class="knob" style="left:75%"></span></div><div class="scale"><span>Poor</span><span>Not Well</span><span>Neutral</span><span>Satisfied</span><span>Great</span></div><div class="note">Enter for feedback</div></section>
   <section class="card"><h2>SMS Experience</h2><div class="slider"><span class="fill" style="width:50%"></span><span class="knob" style="left:50%"></span></div><div class="scale"><span>Poor</span><span>Not Well</span><span>Neutral</span><span>Satisfied</span><span>Great</span></div><div class="note">Enter for feedback</div></section>
   <section class="card"><h2>Data Experience</h2><div class="slider"><span class="fill" style="width:75%"></span><span class="knob" style="left:75%"></span></div><div class="scale"><span>Poor</span><span>Not Well</span><span>Neutral</span><span>Satisfied</span><span>Great</span></div><div class="note">Enter for feedback</div></section>
   <section class="card"><h2>Streaming Experience</h2><div class="slider"><span class="fill" style="width:100%"></span><span class="knob" style="left:100%"></span></div><div class="scale"><span>Poor</span><span>Not Well</span><span>Neutral</span><span>Satisfied</span><span>Great</span></div><div class="note">Enter for feedback</div></section>
  </div>
  <div class="btn">Submit</div>
  <div class="home-bar"></div>
 </div>
</div>

<!-- ===== Large: menu ===== -->
<div class="screen" style="left:120px;top:2072px;width:400px;height:1008px">
 <div class="menu">
  <div class="drawer">
   <div class="status"><span>9:41</span></div>
   <div class="brand"><span class="brand-dot"></span><span class="brand-name">Meridian<br>Signal</span></div>
   <ul class="nav">
    <li><svg width="16" height="16" viewBox="0 0 16 16" fill="none" stroke="#5a6788" stroke-width="1.4"><rect x="1" y="1" width="5.5" height="5.5" rx="1"/><rect x="9.5" y="1" width="5.5" height="5.5" rx="1"/><rect x="1" y="9.5" width="5.5" height="5.5" rx="1"/><rect x="9.5" y="9.5" width="5.5" height="5.5" rx="1"/></svg>Dashboard</li>
    <li><svg width="16" height="16" viewBox="0 0 16 16" fill="none" stroke="#5a6788" stroke-width="1.4"><path d="M2 14l1-4 8-8 3 3-8 8z"/></svg>Edit Profiles</li>
    <li class="active"><svg width="16" height="16" viewBox="0 0 16 16" fill="none" stroke="#1f86d6" stroke-width="1.4"><circle cx="8" cy="8" r="6.5"/><path d="M8 4v4l3 2"/></svg>Survey Interval Timer</li>
    <li><svg width="16" height="16" viewBox="0 0 16 16" fill="none" stroke="#5a6788" stroke-width="1.4"><circle cx="12" cy="3.5" r="2"/><circle cx="4" cy="8" r="2"/><circle cx="12" cy="12.5" r="2"/><path d="M5.8 7l4.4-2.5M5.8 9l4.4 2.5"/></svg>Share this App</li>
    <li><svg width="16" height="16" viewBox="0 0 16 16" fill="none" stroke="#5a6788" stroke-width="1.4"><path d="M3 1.5h3l1.5 3.5-2 1.3a9 9 0 0 0 4.2 4.2l1.3-2 3.5 1.5v3c0 .8-.7 1.5-1.5 1.5A12.5 12.5 0 0 1 1.5 3c0-.8.7-1.5 1.5-1.5z"/></svg>Contact Us</li>
    <li><svg width="16" height="16" viewBox="0 0 16 16" fill="none" stroke="#5a6788" stroke-width="1.4"><circle cx="8" cy="8" r="6.5"/><path d="M6 6a2 2 0 1 1 2.8 1.8c-.5.3-.8.7-.8 1.3M8 11.5v.5"/></svg>Help</li>
    <li><svg width="16" height="16" viewBox="0 0 16 16" fill="none" stroke="#5a6788" stroke-width="1.4"><path d="M6 2H2v12h4M10 4.5L13.5 8 10 11.5M13.5 8H5.5"/></svg>Exit</li>
   </ul>
  </div>
  <div class="peek">
   <div class="survey" style="height:1008px">
    <div class="burger"><i></i><i></i><i></i></div>
    <div class="cards">
     <section class="card"><h2>Call Experience</h2><div class="slider"><span class="fill" style="width:75%"></span><span class="knob" style="left:75%"></span></div><div class="scale"><span>Poor</span><span>Not Well</span><span>Neutral</span><span>Satisfied</span><span>Great</span></div><div class="note">Enter for feedback</div></section>
     <section class="card"><h2>SMS Experience</h2><div class="slider"><span class="fill" style="width:50%"></span><span class="knob" style="left:50%"></span></div><div class="scale"><span>Poor</span><span>Not Well</span><span>Neutral</span><span>Satisfied</span><span>Great</span></div><div class="note">Enter for feedback</div></section>
     <section class="card"><h2>Data Experience</h2><div class="slider"><span class="fill" style="width:75%"></span><span class="knob" style="left:75%"></span></div><div class="scale"><span>Poor</span><span>Not Well</span><span>Neutral</span><span>Satisfied</span><span>Great</span></div><div class="note">Enter for feedback</div></section>
    </div>
   </div>
  </div>
  <div class="home-bar" style="z-index:3"></div>
 </div>
</div>
</body>
</html>
```